Quorvel Lab - Business Cards & Stationary
Layouts for B-cards, Letterhead, Powerpoint Templates
Quorvel Lab - Business Cards & Stationary -
Creative Brief
Professional
Desmond Pelly
Director of Product Development
4852 Amberfield Lane Dallas, Texas 75391-4418
des.pelly@quorvellabs.example

```html
<!DOCTYPE html>
<html lang="en">
<head>
<meta charset="utf-8">
<title>Quorvel Lab – Stationery</title>
<link href="https://fonts.googleapis.com/css2?family=Open+Sans:wght@400;600;700&display=swap" rel="stylesheet">
<style>
  :root {
    --bg: #ecebe8;
    --paper: #ffffff;
    --ink: #2b2b2b;
    --muted: #6d6d6d;
    --brand: #5a3b22;
    --accent: #8e1b1b;
    --band: #4a3320;
    --shade: #f1f0ee;
  }
  * { margin: 0; padding: 0; box-sizing: border-box; }
  html, body { width: 1200px; height: 1044px; overflow: hidden; }
  body {
    background: var(--bg);
    font-family: "Open Sans", Arial, sans-serif;
    color: var(--ink);
    position: relative;
  }
  .sheet {
    position: absolute;
    background: var(--paper);
    box-shadow: 0 3px 10px rgba(0,0,0,.18);
    overflow: hidden;
  }
  .brand-name {
    display: inline-flex; align-items: center; gap: 8px;
    color: var(--brand); font-weight: 700; letter-spacing: .5px;
    white-space: nowrap;
  }
  .brand-name .mark { width: .8em; height: .8em; background: var(--brand); }

  /* slides */
  .slide { left: 164px; width: 311px; height: 261px; }
  .slide-title { top: 113px; }
  .slide-content { top: 399px; height: 246px; }
  .slide-thanks { top: 682px; height: 246px; }

  .slide-title .brand-name { position: absolute; left: 24px; top: 80px; font-size: 30px; }
  .slide-title .title { position: absolute; left: 0; right: 0; top: 160px; text-align: center; font-size: 15px; font-weight: 700; }
  .slide-title .subtitle { position: absolute; left: 0; right: 0; top: 180px; text-align: center; font-size: 9px; color: var(--muted); }
  .slide-title .tagline { position: absolute; left: 0; right: 0; top: 236px; text-align: center; font-size: 9px; color: var(--muted); letter-spacing: .5px; }

  .slide-content .header { position: absolute; left: 12px; top: 12px; font-size: 12px; font-weight: 700; }
  .slide-content .desc { position: absolute; left: 12px; top: 28px; font-size: 8px; color: var(--muted); }
  .slide-content .rule { position: absolute; left: 12px; right: 12px; top: 42px; height: 1px; background: #cfcfcf; }
  .group { position: absolute; left: 12px; width: 150px; }
  .group h4 { font-size: 8px; font-weight: 700; display: flex; align-items: center; gap: 6px; }
  .group h4::before { content: ""; width: 7px; height: 7px; border-radius: 50%; background: var(--brand); }
  .group p { font-size: 6.5px; color: var(--muted); margin-top: 3px; line-height: 1.35; }
  .placeholder { position: absolute; left: 168px; top: 60px; width: 118px; height: 150px; background: var(--shade); border: 1px solid #dedede; }
  .slide-content .foot-brand { position: absolute; right: 10px; bottom: 6px; font-size: 8px; }
  .slide-stripe { position: absolute; left: 0; right: 0; bottom: 0; height: 6px; background: linear-gradient(90deg, #e4e2de 0%, #e4e2de 55%, var(--accent) 75%, var(--band) 100%); }

  .slide-thanks .brand-name { position: absolute; left: 0; right: 0; top: 90px; justify-content: center; font-size: 26px; }
  .slide-thanks .thanks { position: absolute; left: 0; right: 0; top: 162px; text-align: center; font-size: 12px; font-weight: 700; }

  /* business cards */
  .card { top: 102px; width: 240px; height: 124px; border-radius: 4px; }
  .card-front { left: 538px; }
  .card-back { left: 808px; background: linear-gradient(180deg, #ffffff, #ececec); }
  .card-front .brand-name { position: absolute; left: 14px; top: 18px; font-size: 20px; }
  .card-front .person { position: absolute; left: 14px; top: 70px; font-size: 7.5px; line-height: 1.35; width: 110px; }
  .card-front .person strong { font-size: 8.5px; display: block; }
  .card-front .contact { position: absolute; left: 128px; top: 62px; font-size: 6px; color: var(--muted); line-height: 1.45; width: 104px; }
  .card-front .card-line { position: absolute; left: 0; right: 0; bottom: 0; height: 4px; background: linear-gradient(90deg, #e4e2de 0%, var(--accent) 60%, var(--band) 100%); }
  .card-back .brand-name { position: absolute; right: 12px; bottom: 12px; font-size: 12px; }

  /* letterhead */
  .letterhead { left: 529px; top: 260px; width: 521px; height: 665px; }
  .letterhead .brand-name { position: absolute; left: 20px; top: 22px; font-size: 34px; }
  .letterhead .contact { position: absolute; left: 20px; top: 78px; font-size: 8px; color: var(--muted); line-height: 1.4; }
  .letterhead .band { position: absolute; left: 0; right: 0; bottom: 0; height: 14px; }
</style>
</head>
<body>

  <section class="sheet slide slide-title">
    <span class="brand-name"><span class="mark"></span>Quorvel Lab</span>
    <h1 class="title">PRESENTATION TITLE</h1>
    <p class="subtitle">Subtitle text</p>
    <p class="tagline">YOUR TAGLINE CAN BE WRITTEN HERE</p>
  </section>

  <section class="sheet slide slide-content">
    <h2 class="header">PRESENTATION HEADER</h2>
    <p class="desc">Description text</p>
    <div class="rule"></div>
    <div class="group" style="top:58px"><h4>Group 1</h4><p>Short summary of the first point goes here.</p></div>
    <div class="group" style="top:108px"><h4>Group 2</h4><p>Short summary of the second point goes here.</p></div>
    <div class="group" style="top:158px"><h4>Group 3</h4><p>Short summary of the third point goes here.</p></div>
    <div class="placeholder" role="img" aria-label="Image or chart area"></div>
    <span class="brand-name foot-brand">Quorvel Lab</span>
    <div class="slide-stripe"></div>
  </section>

  <section class="sheet slide slide-thanks">
    <span class="brand-name"><span class="mark"></span>Quorvel Lab</span>
    <p class="thanks">THANK YOU FOR YOUR TIME</p>
  </section>

  <section class="sheet card card-front">
    <span class="brand-name"><span class="mark"></span>Quorvel Lab</span>
    <div class="person"><strong>Desmond Pelly</strong>Director of Product Development</div>
    <div class="contact">4852 Amberfield Lane<br>Dallas, Texas 75391-4418<br>Cell: 214.555.0187<br>des.pelly@quorvellabs.example</div>
    <div class="card-line"></div>
  </section>

  <section class="sheet card card-back">
    <span class="brand-name">Quorvel Lab</span>
  </section>

  <section class="sheet letterhead">
    <span class="brand-name"><span class="mark"></span>Quorvel Lab</span>
    <div class="contact">4852 Amberfield Lane, Dallas, Texas 75391-4418<br>Cell: 214.555.0187<br>Email: des.pelly@quorvellabs.example</div>
    <svg class="band" viewBox="0 0 521 14" preserveAspectRatio="none" aria-hidden="true">
      <rect x="0" y="4" width="521" height="10" fill="var(--band)"/>
      <polygon points="330,14 360,0 521,0 521,14" fill="var(--accent)"/>
      <polygon points="400,14 425,4 521,4 521,14" fill="var(--band)"/>
    </svg>
  </section>

</body>
</html>
```